Company brochure for our unique consulting business

We are a small consulting business offering a unique set of services to our clients.. In simple terms we are a business improvement consultancy helping our clients get the best out of their businesses. We work with clients across multiple sectors and deliver a variety of services. We want to put together a brochure to cover these main themes:1. Who we are2. What we do3. The type of people we employ4. The sectors we work inWhile the brochure needs to have a certain corporate feel to it, we don't want it to be "boring" or "stiff". We would like it to have a slightly "friendly" or "informal" feel to it, to reflect the type of organisation we are.We have a company website http://kellbrookadvisory.example , however we do not want to directly replicate the content or feel as we recognise it needs updating.We would like the brochure to be A4 portrait format. We anticipate requiring 12 sides (including covers) but we are happy to be guided on this based on the content we have provided.The attached ppt file gives the detail of the content to be included and also shows the proposed pagination. For the front cover we would like to try 2 versions, one with the KBA logo and one with the Kellbrook Advisory logo (a file of both is attached)One of the most important pages will be the "Our Services" page. We would like this to cover the centre fold. In the ppt file we have shown an example layout, but this is where we need most help - we are clearly not graphic designers! This page will be the most used page in sales meetings etc.Also attached is the following:1. file for our KellBrook Advisory company logo.2. File for our KBA company logo3. Files for Derek's signatures (for under photos) - Owen's to follow4. Photo of Derek & Owen (person in purple shirt to be cropped out)Thank you and really excited to see what everyone comes back with.Derek & Owen

Target Market(s)

Very broad - Manufacturing, Healthcare, Hospitality

Industry/Entity Type

Management Consulting

Font styles to use
Other font styles liked:
• We use Swiss721, but happy to be guided by designer

Colors
3276b5
85abd2
0355a3
333333
5c5c5c
9d9d9d
d9d9d9

Requirements
Must have
• Corporate feel
Nice to have
• Slightly friendly feel
• Our standard "blue" is (CORRECTION) - R55 G96 B146 #376092 and our standard grey is R197 G178, B179 - #B3B2B2, which we would like to keep, but other colours we are happy to be guided on. Brand guidelines attached.

```html
<!DOCTYPE html>
<html lang="en">
<head>
<meta charset="utf-8">
<title>Kellbrook Advisory – Brochure Cover</title>
<link href="https://fonts.googleapis.com/css2?family=Open+Sans:wght@300;400;700;800&display=swap" rel="stylesheet">
<style>
  :root {
    --brand-blue: #3276b5;
    --brand-blue-deep: #0355a3;
    --brand-blue-light: #85abd2;
    --ink: #333333;
    --ink-soft: #5c5c5c;
    --band-dark: #3a3b3d;
    --paper: #ffffff;
    --paper-tint: #f1f2f4;
    --stage: #e4e5e7;
  }
  * { box-sizing: border-box; margin: 0; padding: 0; }
  html, body { width: 1200px; height: 790px; overflow: hidden; }
  body {
    background: var(--stage);
    font-family: "Open Sans", Arial, sans-serif;
    display: flex; align-items: center; justify-content: center;
  }
  .cover {
    position: relative;
    width: 524px; height: 740px;
    background: var(--paper);
    overflow: hidden;
    box-shadow: 0 6px 18px rgba(0,0,0,.15);
  }
  .cover__header {
    position: absolute; left: 0; top: 0; width: 100%; height: 162px;
    background: var(--paper-tint);
  }
  .cover__accent-block {
    position: absolute; left: 0; top: 62px; width: 124px; height: 100px;
    background: linear-gradient(160deg, var(--brand-blue), var(--brand-blue-deep));
  }
  .brand {
    position: absolute; left: 190px; top: 62px;
    display: flex; align-items: center; gap: 14px;
  }
  .brand__mark { width: 30px; height: 30px; background: var(--brand-blue); }
  .brand__name {
    font-weight: 800; font-size: 62px; line-height: 1; letter-spacing: -1px;
    color: var(--ink);
  }
  .cover__photo {
    position: absolute; left: 0; top: 162px; width: 100%; height: 372px;
    background: linear-gradient(180deg, #dfe3e8 0%, #c9d2dc 35%, #8a97a8 65%, #b9c0c6 100%);
  }
  .cover__side-stripe {
    position: absolute; right: 0; top: 330px; width: 40px; height: 300px;
    background: linear-gradient(180deg, var(--brand-blue), var(--brand-blue-deep));
  }
  .cover__band {
    position: absolute; left: 0; bottom: 0; width: calc(100% - 40px); height: 224px;
    background: var(--band-dark);
    padding: 38px 36px 0 44px;
    color: var(--paper);
  }
  .cover__band-foot {
    position: absolute; left: 0; right: -40px; bottom: 0; height: 110px;
    background: var(--band-dark);
  }
  .tagline { position: relative; font-size: 26px; line-height: 1.2; }
  .tagline__lead { font-weight: 800; display: block; }
  .tagline__name-strong { font-weight: 800; }
  .tagline__name-light { font-weight: 300; }
  .tagline__rule {
    display: block; width: 42px; height: 5px; margin: 14px 0 18px;
    background: var(--brand-blue);
  }
  .web {
    position: relative;
    display: flex; align-items: center; gap: 10px;
    font-size: 15px; font-weight: 400; color: var(--paper);
  }
  .web strong { font-weight: 700; }
</style>
</head>
<body>
  <article class="cover">
    <header class="cover__header"></header>
    <div class="cover__accent-block"></div>
    <div class="brand">
      <span class="brand__mark"></span>
      <span class="brand__name">kba</span>
    </div>

    <div class="cover__photo" role="img" aria-label="Photo of four consultants meeting around a table, two shaking hands beside a laptop"></div>
    <div class="cover__side-stripe"></div>

    <div class="cover__band-foot"></div>
    <section class="cover__band">
      <h1 class="tagline">
        <span class="tagline__lead">business improvement by</span>
        <span class="tagline__name-strong">kellbrook</span><span class="tagline__name-light">advisory</span>
      </h1>
      <span class="tagline__rule"></span>
      <p class="web">
        <svg width="16" height="16" viewBox="0 0 16 16" aria-hidden="true">
          <g fill="none" stroke="#3276b5" stroke-width="1.4">
            <circle cx="8" cy="8" r="6.5"/>
            <ellipse cx="8" cy="8" rx="3" ry="6.5"/>
            <line x1="1.5" y1="8" x2="14.5" y2="8"/>
          </g>
        </svg>
        <span>www.<strong>kellbrook</strong>advisory.example</span>
      </p>
    </section>
  </article>
</body>
</html>
```